April 11th Event- Islamorada- Coaching/Tarot/Hypnotherapy

Hi! Need a flyer that can also be posted on social media. Directions attached. Also will need a version that 2 can fit on 1 piece of paper so I can cut in half for hand outs. PDF example attached as well so you can understand. Thank you!

AAAAAAAAAAAAAAAAAAAAAAAAAAAAAAAAAAAAAAAAAAAAAAAAAAAAAAAAAAAAAAAAAAAAAAAAAAAAAAAAAAAAAAAAAAAAAAAAAAAAAAAAAAAAAAAAAAAAAAAAAAAAAAAAAAAAAAAAAAAAAAAAAAAAAAAAAAAAAAAAAAAAAAAAAAAAAAAAAAAAAAAAAAAAAAAAAAAAAAAAAAAAAAAAAAAAAAAAAAAAAAAAAA

Target Market(s)

Female audience age 35-70.
Spiritual, sophisticated

Industry/Entity Type

Event Planning

Font styles to use
Serif

Colors
d2a4cc
3176b5
85acd3
b868aa
e667a6
eea4c8
f59296
fbf289
add136

Requirements
Must have
• See attachments
Nice to have
• See attachments

```html
<!DOCTYPE html>
<html lang="en">
<head>
<meta charset="utf-8">
<title>Get the 411 – An Evening of Self Discovery</title>
<link rel="stylesheet" href="https://fonts.googleapis.com/css2?family=Kaushan+Script&family=EB+Garamond:ital,wght@0,400;0,500;1,400&family=Courier+Prime:wght@400;700&display=swap">
<style>
  :root {
    --paper: #efece4;
    --paper-edge: #e4e0d6;
    --plum: #74506e;
    --teal: #7fb0b6;
    --ink: #4a4a4a;
    --grey: #5a5a5a;
    --box-line: #8fb1b5;
    --box-fill: #d8e3e1;
    --band: #d3dfde;
    --ribbon: #d99ab4;
    --rose: #d9658f;
    --blush: #e9b8c4;
    --berry: #5a3a78;
  }
  * { margin: 0; padding: 0; box-sizing: border-box; }
  html, body { width: 777px; height: 1200px; overflow: hidden; background: var(--paper); }
  .flyer {
    position: relative; width: 777px; height: 1200px; overflow: hidden;
    background: radial-gradient(ellipse at 50% 40%, #f3f1ea 0%, var(--paper) 60%, var(--paper-edge) 100%);
    font-family: "EB Garamond", Georgia, serif; color: var(--ink);
  }
  .tagline { position: absolute; left: 0; top: 0; width: 777px; height: 140px; }
  .tagline text { font-family: "Kaushan Script", cursive; font-size: 31px; fill: var(--ink); }
  .title-get, .title-the, .title-411 { position: absolute; font-family: "Kaushan Script", cursive; line-height: 1; }
  .title-get { left: 146px; top: 92px; font-size: 112px; color: var(--teal); }
  .title-the { left: 204px; top: 206px; font-size: 70px; color: var(--teal); }
  .title-411 { left: 282px; top: 62px; font-size: 262px; color: var(--plum); letter-spacing: -14px; }
  .floral-spray {
    position: absolute; left: 44px; top: 262px; width: 660px; height: 220px;
    background: radial-gradient(ellipse 18% 40% at 52% 52%, var(--rose) 0%, rgba(217,101,143,.7) 55%, transparent 100%),
                radial-gradient(ellipse 14% 34% at 72% 50%, var(--blush) 0%, transparent 100%),
                radial-gradient(ellipse 12% 30% at 88% 30%, rgba(90,58,120,.55) 0%, transparent 100%),
                radial-gradient(ellipse 50% 35% at 35% 58%, rgba(190,140,140,.55) 0%, transparent 100%);
    border-radius: 50%;
  }
  .invite {
    position: absolute; left: 0; top: 484px; width: 777px; text-align: center;
    font-family: "Courier Prime", monospace; font-size: 21px; letter-spacing: 3.6px; line-height: 29px; color: var(--ink);
  }
  .details {
    position: absolute; left: 142px; top: 554px; width: 490px; height: 292px;
    border: 2px solid var(--box-line); padding: 8px;
  }
  .details-inner { width: 100%; height: 100%; background: var(--box-fill); text-align: center; padding-top: 26px; }
  .detail-row { font-size: 27px; line-height: 30px; color: #3d3d3d; }
  .detail-label { font-family: "Kaushan Script", cursive; color: var(--plum); font-size: 27px; margin-right: 8px; }
  .detail-sub { font-style: italic; font-size: 22px; line-height: 27px; color: #4a4a4a; }
  .row-time { margin-top: 22px; }
  .row-where { margin-top: 22px; }
  .floral-accent {
    position: absolute; left: 76px; top: 790px; width: 120px; height: 96px;
    background: radial-gradient(ellipse 28% 30% at 50% 50%, #e07aa0 0%, rgba(233,184,196,.6) 60%, transparent 100%),
                radial-gradient(ellipse 40% 22% at 40% 70%, rgba(190,140,140,.5) 0%, transparent 100%);
    border-radius: 50%;
  }
  .speakers-ribbon { position: absolute; left: 222px; top: 852px; width: 316px; height: 72px; }
  .speakers-ribbon text { font-family: "Kaushan Script", cursive; font-size: 34px; fill: var(--plum); }
  .speaker-list {
    position: absolute; left: 0; top: 940px; width: 777px; text-align: center;
    font-family: "Courier Prime", monospace; font-size: 13.5px; line-height: 20px; color: var(--plum); white-space: nowrap;
  }
  .speaker-name { font-weight: 700; }
  .tickets {
    position: absolute; left: 48px; top: 1015px; width: 680px; height: 30px;
    background: var(--band); border-radius: 3px 14px 4px 12px;
    font-style: italic; font-size: 21.5px; line-height: 30px; text-align: center; color: #5d6f70;
  }
  .contact {
    position: absolute; left: 0; top: 1066px; width: 777px; text-align: center;
    font-family: "Courier Prime", monospace; font-size: 18px; line-height: 24px; letter-spacing: .6px; color: var(--grey);
  }
  .sign-off { position: absolute; left: 0; top: 1132px; width: 777px; text-align: center; }
  .sign-off-text { font-family: "Kaushan Script", cursive; font-size: 25px; color: var(--plum); margin: 0 12px; vertical-align: middle; }
  .chevrons { vertical-align: middle; }
</style>
</head>
<body>
<main class="flyer">
  <svg class="tagline" viewBox="0 0 777 140" aria-label="Open yourself up to the info you have inside!">
    <defs><path id="tagline-arc" d="M 88 116 Q 380 22 692 110"/></defs>
    <text><textPath href="#tagline-arc" startOffset="50%" text-anchor="middle">Open yourself up to the info you have inside!</textPath></text>
  </svg>

  <div class="title-411">411</div>
  <div class="title-get">Get</div>
  <div class="title-the">the</div>

  <div class="floral-spray" role="img" aria-label="Watercolour spray of pink roses, purple berries, leaves and feathers"></div>

  <p class="invite">PLEASE JOIN US FOR AN EVENING OF<br>SELF DISCOVERY, ENLIGHTMENT AND FUN!</p>

  <section class="details">
    <div class="details-inner">
      <p class="detail-row"><span class="detail-label">When:</span>Thursday, April 11th, 2019</p>
      <p class="detail-row row-time"><span class="detail-label">Time:</span>Doors Open at 5:30pm</p>
      <p class="detail-sub">(Event from 6pm-8pm)</p>
      <p class="detail-row row-where"><span class="detail-label">Where:</span>The Gardens at Palm Hollow</p>
      <p class="detail-sub">80410 Coral Reef Road Islamorada</p>
      <p class="detail-sub">(MM81 Bayside behind Harbor Market)</p>
    </div>
  </section>

  <div class="floral-accent" role="img" aria-label="Small watercolour rose with berries and leaves"></div>

  <svg class="speakers-ribbon" viewBox="0 0 316 72" aria-label="Speakers:">
    <g fill="none" stroke="var(--ribbon)" stroke-width="3" stroke-linejoin="round">
      <path d="M 2 30 L 50 30 L 50 62 L 2 62 L 20 46 Z"/>
      <path d="M 314 14 L 266 14 L 266 46 L 314 46 L 296 30 Z"/>
      <path d="M 46 22 Q 160 10 270 8 L 270 42 Q 160 44 46 56 Z" fill="var(--paper)"/>
    </g>
    <text x="160" y="44" text-anchor="middle">Speakers:</text>
  </svg>

  <div class="speaker-list">
    <p>· <span class="speaker-name">MARISA DALE</span> - The Bright Path Life Coach- Certified Professional Life Coach</p>
    <p>· <span class="speaker-name">CORINNE HALLOWAY</span> - Licensed Hypnotherapist- Moonstone Holistic Gifts and Therapies</p>
    <p>· <span class="speaker-name">JUNE SORRELL</span> - Tarot Readings/ Clear Way Spiritual Counselor</p>
  </div>

  <p class="tickets">Tickets $15 each. Drinks included. Names must be on the guest list.</p>

  <p class="contact">Contact Marisa Dale for tickets:<br>Marisa@thebrightpathcoach.com / 305.555.0148</p>

  <div class="sign-off">
    <svg class="chevrons" width="66" height="26" viewBox="0 0 66 26" aria-hidden="true">
      <g fill="none" stroke="#a9c7cb" stroke-width="5"><path d="M4 3 L16 13 L4 23"/><path d="M22 3 L34 13 L22 23"/><path d="M40 3 L52 13 L40 23"/></g>
    </svg><span class="sign-off-text">Hope to see you there!</span><svg class="chevrons" width="66" height="26" viewBox="0 0 66 26" aria-hidden="true">
      <g fill="none" stroke="#a9c7cb" stroke-width="5"><path d="M26 3 L14 13 L26 23"/><path d="M44 3 L32 13 L44 23"/><path d="M62 3 L50 13 L62 23"/></g>
    </svg>
  </div>
</main>
</body>
</html>
```